Business Card Design Project

I need some business cards with the logo you did for us (attached)
I am looking for a coulourful yet serious business card

We do market research
on the back I want the logo

on the front my name : Corinne Valdessac
position : Manager
address : Brume Analytica Sarl - 27 Rue des tanneurs
1847 Glarency - Switzerland
corinne.valdessac@brumeanalytica.ch
Tel : +4122 934 07 58
Mob France :+33 671 42 8356
Mob Italy +39 347 520 8163

The tree of the logo could also be used alone

THE BACKGROUND COLOR ON THE FRONT HAS TO BE WHITE, ON THE BACK YU CAN TRY OHER COLOUR BUT HOMOGENEOUS (NOT EXPENSIVE TO PRINT)

Target Market(s)

multinational companies or other market research companies

Industry/Entity Type

Market Research

Requirements
Must have
• logo on the back
and all the info above

```html
<!DOCTYPE html>
<html lang="en">
<head>
<meta charset="utf-8">
<title>Brume Analytica – Business Cards</title>
<link rel="stylesheet" href="https://fonts.googleapis.com/css2?family=Open+Sans:wght@400;600&display=swap">
<style>
  :root {
    --page: #e9e9e7;
    --teal: #1f6563;
    --teal-soft: #2c7472;
    --white: #ffffff;
    --name-grey: #7a7a7a;
    --text-dark: #4a4a4a;
    --brand-pink: #d8245f;
    --icon-grey: #9aa3a2;
    --note-grey: #8fa9a8;
    --stripe-lime: #eef3cf;
    --stripe-yellow: #f7f1c8;
    --stripe-pink: #f6d3e0;
    --stripe-blue: #d6dcf1;
    --stripe-lilac: #ead6ee;
  }
  * { box-sizing: border-box; margin: 0; padding: 0; }
  html, body {
    width: 1200px; height: 900px; overflow: hidden;
    background: var(--page);
    font-family: "Open Sans", Arial, sans-serif;
  }
  .canvas { position: relative; width: 1200px; height: 900px; }

  /* ---------- Front ---------- */
  .card-front {
    position: absolute; left: 73px; top: 73px;
    width: 548px; height: 343px;
    background: var(--white);
    border-radius: 26px 0 0 26px;
    overflow: hidden;
    box-shadow: 0 4px 14px rgba(0,0,0,.18);
  }
  .front-band {
    position: absolute; left: 0; top: 0; bottom: 0; width: 129px;
    background: var(--teal);
  }
  .front-brand {
    position: absolute; left: 0; width: 129px; bottom: 30px;
    text-align: center; color: var(--white);
    font-size: 14px; font-weight: 400; letter-spacing: .2px;
  }
  .front-brand-dot {
    display: block; width: 30px; height: 30px; margin: 0 auto 6px;
    border-radius: 50%; background: var(--white);
  }
  .stripes { position: absolute; left: 401px; top: 0; bottom: 0; display: flex; gap: 10px; }
  .stripes span { display: block; width: 8px; height: 100%; }
  .stripe-lime { background: var(--stripe-lime); }
  .stripe-yellow { background: var(--stripe-yellow); }
  .stripe-pink { background: var(--stripe-pink); }
  .stripe-blue { background: var(--stripe-blue); }
  .stripe-lilac { background: var(--stripe-lilac); }

  .identity {
    position: absolute; left: 138px; top: 118px;
    display: flex; flex-direction: column; align-items: flex-end;
  }
  .identity-name { font-size: 27px; color: var(--name-grey); font-weight: 400; line-height: 1.1; }
  .identity-role { font-size: 16px; color: var(--teal); letter-spacing: .5px; line-height: 1.2; }

  .front-email {
    position: absolute; left: 138px; bottom: 14px;
    display: flex; align-items: center; gap: 7px;
    font-size: 16px; color: var(--text-dark);
  }
  .icon-box {
    width: 20px; height: 20px; border-radius: 4px;
    background: var(--icon-grey); display: inline-flex; align-items: center; justify-content: center;
  }
  .front-email .icon-box { background: var(--teal-soft); }

  /* ---------- Back ---------- */
  .card-back {
    position: absolute; left: 621px; top: 477px;
    width: 549px; height: 341px;
    background: var(--teal);
    border-radius: 30px 0 30px 0;
    box-shadow: 0 4px 14px rgba(0,0,0,.25);
    color: var(--white);
  }
  .back-brand {
    position: absolute; left: 0; right: 0; top: 150px;
    text-align: center; padding-left: 90px;
    font-size: 44px; font-weight: 400; color: var(--brand-pink);
    letter-spacing: -.5px;
  }
  .back-address {
    position: absolute; left: 13px; top: 249px;
    display: flex; gap: 8px; font-size: 16px; line-height: 1.35;
  }
  .back-address .line-indent { padding-left: 10px; }
  .back-address .line-outdent { margin-left: -4px; }
  .back-phones {
    position: absolute; left: 320px; top: 249px;
    list-style: none; font-size: 16px; line-height: 1.35;
  }
  .back-phones li { display: flex; align-items: center; gap: 6px; margin-bottom: 2px; }
  .phone-note { font-size: 9px; color: var(--note-grey); align-self: flex-end; margin-bottom: 3px; margin-left: -3px; }
</style>
</head>
<body>
<main class="canvas">

  <section class="card-front" aria-label="Card front">
    <div class="front-band">
      <p class="front-brand"><span class="front-brand-dot"></span>brume analytica</p>
    </div>
    <div class="stripes" aria-hidden="true">
      <span class="stripe-lime"></span><span class="stripe-yellow"></span><span class="stripe-yellow"></span>
      <span class="stripe-pink"></span><span class="stripe-blue"></span><span class="stripe-pink"></span>
      <span class="stripe-lilac"></span>
    </div>
    <div class="identity">
      <h1 class="identity-name">Corinne Valdessac</h1>
      <p class="identity-role">MANAGER</p>
    </div>
    <p class="front-email">
      <span class="icon-box">
        <svg width="14" height="14" viewBox="0 0 14 14" fill="none" stroke="#fff" stroke-width="1.2">
          <circle cx="7" cy="7" r="5.5"/><ellipse cx="7" cy="7" rx="2.4" ry="5.5"/><path d="M1.5 7h11"/>
        </svg>
      </span>
      corinne.valdessac@brumeanalytica.ch
    </p>
  </section>

  <section class="card-back" aria-label="Card back">
    <p class="back-brand">brume analytica</p>

    <div class="back-address">
      <span class="icon-box">
        <svg width="14" height="14" viewBox="0 0 14 14" fill="#fff">
          <path d="M7 1.5 1 7h2v5.5h3V9h2v3.5h3V7h2z"/>
        </svg>
      </span>
      <address style="font-style:normal">
        Brume Analytica Sarl<br>
        <span class="line-indent">- 27 Rue des tanneurs</span><br>
        <span class="line-outdent">1847 Glarency - Switzerland.</span>
      </address>
    </div>

    <ul class="back-phones">
      <li>
        <span class="icon-box">
          <svg width="14" height="14" viewBox="0 0 14 14" fill="#fff">
            <path d="M2 4c0-1.5 2-2.5 5-2.5s5 1 5 2.5v1H9.5V4h-5v1H2zM3 6.5h8l1 5.5H2z"/>
          </svg>
        </span>+4122 934 07 58
      </li>
      <li>
        <span class="icon-box">
          <svg width="14" height="14" viewBox="0 0 14 14" fill="#fff">
            <rect x="4" y="1" width="6" height="12" rx="1"/><rect x="5" y="3" width="4" height="5" fill="#9aa3a2"/>
          </svg>
        </span>+33 671 42 8356 <span class="phone-note">(France)</span>
      </li>
      <li>
        <span class="icon-box">
          <svg width="14" height="14" viewBox="0 0 14 14" fill="#fff">
            <rect x="4" y="1" width="6" height="12" rx="1"/><rect x="5" y="3" width="4" height="5" fill="#9aa3a2"/>
          </svg>
        </span>+39 347 520 8163 <span class="phone-note">(Italy)</span>
      </li>
    </ul>
  </section>

</main>
</body>
</html>
```